Graphic Design of Business Process

We require an eye-catching, sophisticated design of 2 business processes (attached), that will be used digitally AND for print (to be put on walls in our office).

The basic layout is attached. We require a creative, professional designer to re-design these so that they look appealing but still able to grasp all the information.

We will require vector files and editable project files for final delivery. You may refer to our website (kitefieldmedia.com.au) for an indication of our brand.

If you have any questions, please ask.

Thank you.

```html
<!DOCTYPE html>
<html lang="en">
<head>
<meta charset="utf-8">
<title>Content Hierarchy</title>
<link rel="stylesheet" href="https://fonts.googleapis.com/css2?family=Archivo+Black&family=Oswald:wght@600&family=Roboto+Condensed:wght@400&family=Open+Sans:wght@700&display=swap">
<style>
  :root {
    --page: #ffffff;
    --board: #000000;
    --red: #e2332b;
    --red-side: #731713;
    --yellow: #ffee00;
    --shadow-grey: #3c3c3c;
    --ink: #1a1a1a;
    --white: #ffffff;
  }
  html, body {
    margin: 0;
    padding: 0;
    width: 1200px;
    height: 1200px;
    overflow: hidden;
    background: var(--page);
  }
  .hierarchy-board { display: block; width: 1200px; height: 1200px; }
  .board-bg { fill: var(--board); }
  .pillar-front { fill: var(--red); }
  .pillar-side { fill: var(--red-side); }
  .pillar-title {
    fill: var(--white);
    font-family: "Oswald", "Roboto Condensed", sans-serif;
    font-weight: 600;
    font-size: 100px;
  }
  .tier-card { fill: var(--yellow); }
  .tier-shadow { fill: var(--shadow-grey); }
  .tier-name {
    fill: var(--ink);
    font-family: "Archivo Black", sans-serif;
    font-size: 62px;
    text-anchor: middle;
  }
  .tier-note {
    fill: var(--ink);
    font-family: "Roboto Condensed", sans-serif;
    font-weight: 400;
    font-size: 33px;
    text-anchor: middle;
  }
  .connector { stroke: var(--yellow); stroke-width: 3.5; fill: none; }
  .connector-head { fill: var(--yellow); }
  .site-url {
    fill: var(--white);
    font-family: "Open Sans", sans-serif;
    font-weight: 700;
    font-size: 27px;
    text-anchor: end;
  }
</style>
</head>
<body>
<svg class="hierarchy-board" viewBox="0 0 1200 1200" xmlns="http://www.w3.org/2000/svg">
  <rect class="board-bg" x="128" y="78" width="958" height="957"/>

  <!-- Title pillar -->
  <polygon class="pillar-side" points="128,290 234,142 234,982 148,1035 128,1035"/>
  <rect class="pillar-front" x="234" y="142" width="184" height="840"/>
  <text class="pillar-title" transform="translate(374,934) rotate(-90)" textLength="758" lengthAdjust="spacingAndGlyphs">CONTENT HIERARCHY</text>

  <!-- Tier shadows -->
  <polygon class="tier-shadow" points="1042,258 1086,258 1086,450 910,450 816,398"/>
  <polygon class="tier-shadow" points="1042,462 1086,462 1086,650 910,650 826,602"/>
  <polygon class="tier-shadow" points="1042,668 1086,668 1086,872 926,872 800,808"/>

  <!-- Tier cards -->
  <path class="tier-card" d="M523,258 H1042 V310 A88,88 0 0 1 954,398 H523 Z"/>
  <path class="tier-card" d="M523,462 H1042 V514 A88,88 0 0 1 954,602 H523 Z"/>
  <path class="tier-card" d="M523,668 H1042 V720 A88,88 0 0 1 954,808 H523 Z"/>

  <text class="tier-name" x="778" y="330">HERO</text>
  <text class="tier-note" x="771" y="372">TENTPOLE CAMPAIGNS</text>

  <text class="tier-name" x="778" y="538">HUB</text>
  <text class="tier-note" x="778" y="581">REGULAR “PUSH” CONTENT</text>

  <text class="tier-name" x="798" y="737">HYGIENE</text>
  <text class="tier-note" x="780" y="778">ALWAYS-ON “PULL” CONTENT</text>

  <!-- Connector -->
  <path class="connector" d="M523,322 H486 V754 H523 M486,530 H523 M486,530 H430"/>
  <polygon class="connector-head" points="392,530 454,502 440,530 454,558"/>

  <text class="site-url" x="1050" y="1008">kitefieldmedia.com.au</text>
</svg>
</body>
</html>
```